Business Card Design Project

I need the following:

Logo -
Name - Dale Whitcomb
Title - Customer Experience Officer
Web - www.brvq.net
Phone - 555-418-3076
Updates

Project Deadline Extended
Reason: I launched the project later than anticipated. I look forward to seeing your designs. Dale

Industry/Entity Type

Business

```html
<!DOCTYPE html>
<html lang="en">
<head>
<meta charset="utf-8">
<title>Dale Whitcomb – Business Card</title>
<link rel="stylesheet" href="https://fonts.googleapis.com/css2?family=Archivo+Black&family=Mulish:wght@300;400;800&display=swap">
<style>
  :root {
    --bg: #2b2b2d;
    --card: #ffffff;
    --card-shade: #eef0f2;
    --blue: #1478b8;
    --blue-deep: #0d5f97;
    --ink: #111111;
    --grey: #4a4a4a;
    --rule: #1f7fc0;
  }
  * { margin: 0; padding: 0; box-sizing: border-box; }
  html, body { width: 1200px; height: 900px; overflow: hidden; }
  body {
    background: var(--bg);
    display: flex; align-items: center; justify-content: center;
    font-family: "Mulish", "Century Gothic", sans-serif;
  }
  .card {
    position: relative;
    width: 1000px; height: 570px;
    background: linear-gradient(135deg, var(--card) 55%, var(--card-shade));
    overflow: hidden;
    box-shadow: 0 20px 50px rgba(0,0,0,.45);
  }
  .brand {
    position: absolute; left: 120px; top: 110px;
    display: flex; align-items: center; gap: 36px;
  }
  .brand-dot {
    width: 150px; height: 150px; border-radius: 50%;
    background: radial-gradient(circle at 35% 30%, #4aa3e0, var(--blue-deep) 70%);
  }
  .brand-text { display: flex; flex-direction: column; align-items: flex-start; }
  .brand-name {
    font-family: "Archivo Black", "Arial Black", sans-serif;
    font-size: 40px; line-height: 0.95; letter-spacing: 2px;
    color: var(--ink); text-transform: uppercase;
  }
  .brand-rule {
    width: 100%; height: 2px; background: var(--rule); margin-top: 10px;
  }
  .brand-web {
    align-self: center; margin-top: 4px;
    font-weight: 800; font-size: 16px; color: var(--blue);
  }
  .person { position: absolute; left: 120px; bottom: 90px; }
  .person-name {
    font-weight: 800; font-size: 48px; color: var(--blue); line-height: 1.1;
  }
  .person-title {
    font-weight: 300; font-size: 32px; color: var(--grey);
  }
  .divider {
    position: absolute; left: 610px; top: 370px;
    width: 4px; height: 80px;
    background: linear-gradient(to bottom, transparent, var(--blue) 30%, var(--blue) 70%, transparent);
  }
  .contact { position: absolute; left: 660px; top: 330px; list-style: none; }
  .contact li {
    display: flex; align-items: center; gap: 22px;
    font-weight: 300; font-size: 32px; color: var(--grey);
    margin-bottom: 28px;
  }
  .contact svg { width: 36px; height: 36px; fill: var(--blue); flex: none; }
  .band {
    position: absolute; right: 0; bottom: 0;
    width: 400px; height: 34px;
    background: linear-gradient(90deg, var(--blue-deep), var(--blue));
    border-top-left-radius: 40px 34px;
  }
</style>
</head>
<body>
  <article class="card">
    <header class="brand">
      <div class="brand-dot"></div>
      <div class="brand-text">
        <div class="brand-name">Bravo Quay<br>Consulting<br>Group</div>
        <div class="brand-rule"></div>
        <div class="brand-web">www.brvq.net</div>
      </div>
    </header>

    <section class="person">
      <h1 class="person-name">Dale Whitcomb</h1>
      <p class="person-title">Customer Experience Officer</p>
    </section>

    <div class="divider"></div>

    <ul class="contact">
      <li>
        <svg viewBox="0 0 24 24" aria-hidden="true"><path d="M3 7c0-2 4-3 9-3s9 1 9 3v2h-5V7.5c-1-.4-2.4-.6-4-.6s-3 .2-4 .6V9H3zM6 11h12l2 8H4zm6 1.5a3 3 0 1 0 0 6 3 3 0 0 0 0-6z"/></svg>
        <span>555-418-3076</span>
      </li>
      <li>
        <svg viewBox="0 0 24 24" aria-hidden="true"><path d="M10 14l-2 2a3 3 0 0 1-4-4l3-3a3 3 0 0 1 4 0l-1.5 1.5a1 1 0 0 0-1 0l-3 3a1 1 0 0 0 1.5 1.5l1.2-1.2zm4-4l2-2a3 3 0 0 1 4 4l-3 3a3 3 0 0 1-4 0l1.5-1.5a1 1 0 0 0 1 0l3-3a1 1 0 0 0-1.5-1.5l-1.2 1.2z"/></svg>
        <span>www.brvq.net</span>
      </li>
    </ul>

    <div class="band"></div>
  </article>
</body>
</html>
```